Stationary for mobile ultrasound company
Business card, letter head and envelope design
Stationary for mobile ultrasound company - Imaging
Modern
Lorna Pettibone, RDMS, ARRT
Owner/Operator
5718 N. Quarry Hollow Ln. McCammon, Idaho 83791
lumenscanhealth@corvilmail.net
www. plinthory.com
Please add tag line under logo: Improving ultrasound in a convenient and personal way.
Appointment time and date spaces. Please try logo as is and with black backgrounds on front of card

```html
<!DOCTYPE html>
<html lang="en">
<head>
<meta charset="utf-8">
<title>Lumenscan Imaging – Business Card</title>
<link href="https://fonts.googleapis.com/css2?family=Open+Sans:wght@400;600;700;800&display=swap" rel="stylesheet">
<style>
  :root {
    --purple: #8a2b9b;
    --purple-deep: #6f1f80;
    --teal: #1f7f8c;
    --ink: #3d3d3d;
    --paper: #ffffff;
    --backdrop: #ecebe8;
  }
  html, body {
    margin: 0;
    width: 1200px;
    height: 914px;
    overflow: hidden;
    background: var(--backdrop);
    font-family: "Open Sans", Arial, sans-serif;
  }
  .card {
    position: absolute;
    left: 100px;
    top: 171px;
    width: 1000px;
    height: 572px;
    box-sizing: border-box;
    background: var(--purple);
    padding: 30px;
    box-shadow: 0 6px 18px rgba(0,0,0,0.18);
  }
  .card-face {
    position: relative;
    width: 100%;
    height: 100%;
    background: var(--paper);
  }
  .brand {
    position: absolute;
    left: 0;
    right: 0;
    top: 120px;
    display: flex;
    justify-content: center;
    align-items: center;
    gap: 16px;
  }
  .brand-mark {
    width: 38px;
    height: 38px;
    border-radius: 50%;
    background: var(--teal);
  }
  .brand-name {
    font-weight: 800;
    font-size: 52px;
    letter-spacing: 1px;
    color: var(--purple);
    text-transform: uppercase;
  }
  .identity {
    position: absolute;
    right: 490px;
    top: 262px;
    text-align: right;
    color: var(--ink);
  }
  .person-name {
    font-size: 27px;
    font-weight: 600;
    color: var(--purple);
    margin: 0;
  }
  .person-role {
    font-size: 20px;
    margin: 2px 0 30px;
  }
  .address {
    font-size: 20px;
    line-height: 1.45;
    font-style: normal;
  }
  .divider {
    position: absolute;
    left: 474px;
    top: 268px;
    width: 2px;
    height: 180px;
    background: var(--purple);
  }
  .contacts {
    position: absolute;
    left: 490px;
    top: 266px;
    margin: 0;
    padding: 0;
    list-style: none;
    color: var(--ink);
    font-size: 20px;
  }
  .contacts li {
    display: flex;
    align-items: center;
    gap: 10px;
    height: 36px;
  }
  .contacts li.small { font-size: 13px; }
  .icon {
    width: 22px;
    height: 22px;
    flex: none;
  }
</style>
</head>
<body>
  <div class="card">
    <div class="card-face">
      <div class="brand">
        <span class="brand-mark"></span>
        <span class="brand-name">Lumenscan Imaging</span>
      </div>

      <div class="identity">
        <p class="person-name">Lorna Pettibone, RDMS, ARRT</p>
        <p class="person-role">Owner/Operator</p>
        <address class="address">5718 N. Quarry Hollow Ln.<br>McCammon, Idaho 83791</address>
      </div>

      <div class="divider"></div>

      <ul class="contacts">
        <li>
          <svg class="icon" viewBox="0 0 22 22"><circle cx="11" cy="11" r="11" fill="#8a2b9b"/><path d="M7 6c1-1 2 0 2.5 1.2s-.6 1.5-.3 2.3c.5 1.2 1.6 2.3 2.8 2.8.8.3 1.2-.8 2.3-.3S16 14 15 15c-2 2-9-5-8-9z" fill="#fff"/></svg>
          (208) 555-0147
        </li>
        <li>
          <svg class="icon" viewBox="0 0 22 22"><circle cx="11" cy="11" r="11" fill="#8a2b9b"/><rect x="8" y="5" width="6" height="12" rx="1.2" fill="#fff"/><rect x="9" y="6.5" width="4" height="7" fill="#8a2b9b"/></svg>
          (208) 555-0192
        </li>
        <li>
          <svg class="icon" viewBox="0 0 22 22"><circle cx="11" cy="11" r="11" fill="#8a2b9b"/><rect x="6" y="9" width="10" height="6" rx="1" fill="#fff"/><rect x="8" y="5.5" width="6" height="4" fill="#fff"/></svg>
          (208) 555-0163
        </li>
        <li class="small">
          <svg class="icon" viewBox="0 0 22 22"><circle cx="11" cy="11" r="11" fill="#8a2b9b"/><rect x="5.5" y="7" width="11" height="8" fill="#fff"/><path d="M5.5 7l5.5 4.5L16.5 7" fill="none" stroke="#8a2b9b" stroke-width="1.2"/></svg>
          lumenscanhealth@corvilmail.net
        </li>
        <li>
          <svg class="icon" viewBox="0 0 22 22"><circle cx="11" cy="11" r="11" fill="#8a2b9b"/><circle cx="11" cy="11" r="5.5" fill="none" stroke="#fff" stroke-width="1.3"/><path d="M5.5 11h11M11 5.5c-2.5 3-2.5 8 0 11M11 5.5c2.5 3 2.5 8 0 11" fill="none" stroke="#fff" stroke-width="1"/></svg>
          www. plinthory.com
        </li>
      </ul>
    </div>
  </div>
</body>
</html>
```